LEAP GLIDE SOAR

Need a 4 X 6 post card design. Here are the elements that need to be on the card:
LEAP, GLIDE, SOAR (This is the title please feel free and create)
DATE: August 28, 2022
Showtimes 2:30 PM & 7:30 PM
Location: Harriet Colvane Theatre Walnut Creek, CA
Tickets can be purchased at:
http://colvanestagehall.tixora-example.com/LEAPGLIDESOAR or
by calling the ticket office at (925) 555-STAGE
LEAP, GLIDE, SOAR showcases the dance stylings of urban hip hop, ballet, modern jazz and much much more! Bay Area renown dancer/choreographer Rosa Janelle Pruitt headlines this cast of dancers and will amaze you as she takes you on a journey through dance that you will never forget. Join us for an experience that will prove to excite and delight you!
Now for the artwork I would like to incorporate all three of these photos. The photo entitled "beach" you are only to use the dancer on the left. So clip out the other dancer in the pink dress. The Garden photo and the beach photo the images need to be cut out from the background. The sidewalk photo you can leave the background (just my preference) but for the sake of the overall design I'm ok with removing its background as well.
Ok have at it. I want to end this competition in a few days so let's get these designs in. Thank you!

```html
<!DOCTYPE html>
<html lang="en">
<head>
<meta charset="utf-8">
<title>Leap Glide Soar – Postcard</title>
<link href="https://fonts.googleapis.com/css2?family=Poppins:wght@400;500;800&family=Lato:wght@400;700&display=swap" rel="stylesheet">
<style>
  :root{
    --page:#f2f2f4;
    --plum-deep:#2a0c33;
    --plum:#4a1442;
    --plum-mid:#5e1750;
    --magenta:#c4176b;
    --berry:#7a1a5e;
    --gold:#fdc316;
    --ink:#2a0c33;
    --white:#ffffff;
  }
  *{margin:0;padding:0;box-sizing:border-box}
  html,body{width:972px;height:1200px;overflow:hidden;background:var(--page)}
  .card{position:absolute;left:151px;width:648px;height:433px;box-shadow:3px 3px 4px rgba(0,0,0,.45);overflow:hidden}
  .front{top:111px;background:var(--plum-deep)}
  .back{top:604px;background:var(--white)}
  .card svg.bg{position:absolute;inset:0}
  .photo{position:absolute}
  .title{position:absolute;right:55px;top:46px;text-align:right;font-family:'Poppins',sans-serif;font-weight:800;color:var(--white);font-size:53px;line-height:49px;letter-spacing:.5px}
  .date{position:absolute;left:409px;top:207px;width:182px;height:39px;background:var(--gold);color:var(--ink);font-family:'Poppins',sans-serif;font-weight:500;font-size:20px;line-height:39px;text-align:center}
  .times{position:absolute;right:57px;top:254px;color:var(--white);font-family:'Poppins',sans-serif;font-weight:500;font-size:25px;white-space:nowrap}
  .venue{position:absolute;right:62px;top:297px;text-align:right;color:var(--white);font-family:'Poppins',sans-serif;font-size:16px;line-height:20px}
  .blurb{position:absolute;left:104px;top:50px;width:312px;color:var(--white);font-family:'Lato',sans-serif;font-size:11.3px;line-height:14.4px;text-align:justify}
  .tickets-label{position:absolute;left:28px;top:288px;color:var(--white);font-family:'Poppins',sans-serif;font-size:12px}
  .tickets-url{position:absolute;left:30px;top:311px;color:var(--gold);font-family:'Poppins',sans-serif;font-size:11.5px;white-space:nowrap}
  .call-label{position:absolute;left:64px;top:362px;color:var(--gold);font-family:'Poppins',sans-serif;font-size:12px}
  .phone{position:absolute;left:64px;top:380px;color:var(--white);font-family:'Lato',sans-serif;font-weight:700;font-size:24px;white-space:nowrap}
  .stamp{position:absolute;left:554px;top:31px;width:62px;height:62px;border:1px solid var(--ink)}
  .address-line{position:absolute;left:463px;width:153px;height:1px;background:var(--ink)}
</style>
</head>
<body>

<section class="card front">
  <svg class="bg" width="648" height="433" viewBox="0 0 648 433">
    <defs>
      <radialGradient id="stageGlow" cx="243" cy="196" r="330" gradientUnits="userSpaceOnUse">
        <stop offset="0" stop-color="var(--magenta)"/>
        <stop offset=".55" stop-color="var(--berry)"/>
        <stop offset="1" stop-color="#4a1250"/>
      </radialGradient>
    </defs>
    <polygon points="476,0 648,0 648,433 0,433 0,380 196,380" fill="var(--berry)" opacity=".55"/>
    <polygon points="0,0 476,0 462,21 26,21 26,410 340,433 0,433" fill="var(--plum-deep)"/>
    <rect x="26" y="21" width="595" height="389" fill="url(#stageGlow)"/>
    <polygon points="26,410 240,410 196,433 0,433 0,380 26,380" fill="var(--berry)" opacity=".7"/>
  </svg>
  <svg class="photo" style="left:136px;top:26px" width="204" height="368" role="img" aria-label="Cut-out photo of a dancer in black leotard and skirt balancing on one leg, arms raised">
    <defs><linearGradient id="dancerOne" x1="0" y1="0" x2="0" y2="1"><stop offset="0" stop-color="#3a1a2c"/><stop offset="1" stop-color="#1a0f18"/></linearGradient></defs>
    <rect width="204" height="368" rx="14" fill="url(#dancerOne)" opacity=".55"/>
  </svg>
  <h1 class="title">LEAP<br>GLIDE<br>SOAR</h1>
  <div class="date">August 28, 2022</div>
  <div class="times">2:30 PM &amp; 7:30 PM</div>
  <p class="venue">Harriet Colvane<br>Theatre Walnut<br>Creek, CA</p>
</section>

<section class="card back">
  <svg class="bg" width="648" height="433" viewBox="0 0 648 433">
    <polygon points="0,0 489,0 403,433 0,433" fill="var(--plum-deep)"/>
    <polygon points="170,15 467,15 398,173 76,173 76,33 170,33" fill="var(--berry)" opacity=".55"/>
    <polygon points="76,33 443,33 408,172 76,172" fill="var(--berry)" opacity=".75"/>
    <polygon points="0,172 434,172 414,273 0,273" fill="var(--plum)"/>
    <rect x="0" y="273" width="420" height="67" fill="var(--plum-deep)"/>
    <polygon points="0,340 418,340 403,433 0,433" fill="var(--plum-mid)"/>
  </svg>
  <svg class="photo" style="left:8px;top:4px" width="88" height="269" role="img" aria-label="Cut-out photo of the headlining choreographer standing in a long pink dress">
    <rect width="88" height="269" rx="10" fill="#d4479c" opacity=".8"/>
  </svg>
  <p class="blurb">LEAP, GLIDE, SOAR showcases the dance stylings of urban hip hop, ballet, modern jazz and much much more! Bay Area renown dancer/choreographer Rosa Janelle Pruitt headlines this cast of dancers and will amaze you as she takes you on a journey through dance that you will never forget. Join us for an experience that will prove to excite and delight you!</p>
  <svg class="photo" style="left:220px;top:161px" width="236" height="272" role="img" aria-label="Cut-out photo of a dancer in white holding a flowing violet scarf overhead">
    <defs><linearGradient id="dancerTwo" x1="0" y1="0" x2="1" y2="1"><stop offset="0" stop-color="#6a4bb0"/><stop offset="1" stop-color="#f4f0f6"/></linearGradient></defs>
    <rect width="236" height="272" rx="14" fill="url(#dancerTwo)" opacity=".75"/>
  </svg>
  <p class="tickets-label">Tickets can be purchased at:</p>
  <p class="tickets-url">colvanestagehall.tixora-example.com/LEAPGLIDESOAR</p>
  <p class="call-label">Or by calling the ticket office at</p>
  <p class="phone">(925) 555-STAGE</p>
  <div class="stamp"></div>
  <div class="address-line" style="top:201px"></div>
  <div class="address-line" style="top:241px"></div>
  <div class="address-line" style="top:281px"></div>
</section>

</body>
</html>
```